Consulting Firm stationery design

Now that the MakerHive has given us a new logo we'll now need to have all our stationery designed. So we're asking for this community to help us once again.We're looking to get from you Letterheads (Header and Footer, suitable to be applied on a .docx format. Vectors are required but keep this in mind), Envelopes (Front and Back designs, back is not a must but desirable depending on your design), 9"x 12" Pocket Folders (consider design for front and back, also for pockets as well), Business Cards.An elegant design is a must have, mostly for Folders and Envelopes. The idea with this two is to stand out from others when they're handed over. Ideas are welcomed, we were thinking maybe on some texturing simulation for these.Folders will have 3 addresses and contact information. Envelopes will have 1 address and contact information.Brand Manual attached. vendaluxo logo has been copyrighted already. I'm also attaching the current stationary designs (these never got to be out for production but was going to be before we made the brand changes); Pocker folders page 1 to 4 (pages 2 and 4 are the pocket designs), Pages 5 and 6 (6 is the back of the envelope), Pages 7 and 8 (8 is the back of the business card). No letterhead within these designs as it just had the logo and address.

Industry/Entity Type

Business Consultant

Font styles to use
Serif
Sans Serif

Requirements
Must have
• Elegance
Nice to have
• Modern looking out of common

```html
<!DOCTYPE html>
<html lang="en">
<head>
<meta charset="utf-8">
<title>vendaluxo stationery</title>
<link href="https://fonts.googleapis.com/css2?family=Poppins:wght@400;600;700&family=Tinos&family=Roboto:wght@400;500&display=swap" rel="stylesheet">
<style>
:root{
  --bg:#a9a8a9;
  --paper:#f3f3f4;
  --blue:#0f74b4;
  --ink:#2c2f3a;
  --grey-text:#55585f;
  --faint:#dfe6ed;
}
*{margin:0;padding:0;box-sizing:border-box}
html,body{width:1200px;height:960px;overflow:hidden;background:var(--bg)}
.canvas{position:relative;width:1200px;height:960px;font-family:"Poppins",sans-serif}
.piece{position:absolute;box-shadow:0 1px 4px rgba(0,0,0,.25);overflow:hidden}
.brand-name{font-family:"Poppins",sans-serif;font-weight:700;color:var(--ink);letter-spacing:-.5px;display:inline-flex;align-items:center;gap:.25em;line-height:1;white-space:nowrap}
.brand-name .dot{width:.4em;height:.4em;border-radius:50%;background:var(--blue);display:inline-block}
.brand-name.light{color:#fff}
.brand-name.light .dot{background:#fff}
.band{position:absolute;left:0;bottom:0;width:100%}
.band-url{position:absolute;right:16px;bottom:6px;color:#fff;font-size:7px;line-height:9px;letter-spacing:3px;font-family:"Poppins",sans-serif;white-space:nowrap}

/* business card front */
.card-front{left:86px;top:70px;width:218px;height:126px;background:var(--blue)}
.card-front .brand-name{position:absolute;left:50%;top:44px;transform:translateX(-50%);font-size:20px}
.card-front .partner-strip{position:absolute;left:0;bottom:11px;width:100%;height:11px;background:var(--ink);display:flex;justify-content:space-between;align-items:center;padding:0 12px}
.partner-badge{background:#fff;opacity:.9;border-radius:2px}

/* business card back */
.card-back{left:337px;top:70px;width:219px;height:126px;background:linear-gradient(135deg,#eeeeef,#dedee0)}
.card-back .contact{position:absolute;left:10px;top:14px;font-size:4.3px;line-height:5.4px;color:var(--grey-text);white-space:nowrap}
.card-back .contact .person{font-size:5.6px;color:var(--ink);font-weight:600}
.card-back .contact .gap{height:3px}
.card-back .contact .link{color:var(--blue)}
.card-back .brand-name{position:absolute;right:16px;top:78px;font-size:15px}
.card-back .tagline{position:absolute;right:10px;bottom:1px;font-size:4.2px;color:#fff;font-weight:600}

/* envelope front */
.envelope-front{left:60px;top:237px;width:562px;height:254px;background:linear-gradient(90deg,#f4f4f5,#ececee)}
.envelope-front .brand-name{position:absolute;left:30px;top:72px;font-size:26px}
.envelope-front .address{position:absolute;left:30px;top:107px;font-size:7.3px;line-height:9.6px;color:var(--grey-text)}
.envelope-front .faint-mark{position:absolute;left:368px;top:85px}

/* envelope back */
.envelope-back{left:56px;top:514px;width:560px;height:254px;background:#f5f5f6}
.envelope-back .texture{position:absolute;left:0;top:0;width:100%;height:100%;background:linear-gradient(180deg,#e9ebee 0%,#f6f6f7 100%)}
.envelope-back .flap{position:absolute;left:0;top:0}
.envelope-back .badges{position:absolute;top:30px;left:144px;display:flex;gap:20px;align-items:center}

/* letterhead */
.letterhead{left:642px;top:30px;width:522px;height:736px;background:linear-gradient(90deg,#f4f4f5,#e9e9eb)}
.letterhead .brand-name{position:absolute;left:50%;top:72px;transform:translateX(-50%);font-size:34px}
.letterhead .faint-mark{position:absolute;left:170px;top:270px}
.letter{position:absolute;left:49px;top:180px;width:431px;font-family:"Tinos",serif;font-size:8.6px;line-height:12px;color:var(--grey-text)}
.letter .date{margin-bottom:24px}
.letter .recipient{margin-bottom:20px}
.letter p.body{text-align:justify;margin-bottom:12px}
.signature{position:absolute;left:50px;top:522px;width:110px;height:50px;background:linear-gradient(90deg,rgba(60,60,70,.12),rgba(60,60,70,.04));border-radius:4px}
.footer{position:absolute;top:662px;left:0;width:100%;font-family:"Roboto",sans-serif;font-size:7.8px;line-height:9.6px;color:#6a6d73}
.footer .col{position:absolute;white-space:nowrap}
.footer .col strong{font-weight:500;color:#55585f}
</style>
</head>
<body>
<div class="canvas">

  <!-- business card front -->
  <section class="piece card-front" role="img" aria-label="Business card front: blue field with a repeating ring pattern">
    <span class="brand-name light">vendaluxo<span class="dot"></span></span>
    <div class="partner-strip">
      <span class="partner-badge" style="width:26px;height:5px"></span>
      <span class="partner-badge" style="width:38px;height:5px"></span>
      <span class="partner-badge" style="width:20px;height:5px"></span>
    </div>
  </section>

  <!-- business card back -->
  <section class="piece card-back">
    <div class="contact">
      <div class="person">Marco T. Reyes <span style="font-weight:400">| COO &amp; Partner</span></div>
      <div>MBA, MSc Systems, Lead Auditor</div>
      <div>Predictive Analytics</div>
      <div class="gap"></div>
      <div>(555) 310 4720 ext. 201</div>
      <div>(555) 310 8841</div>
      <div>marco@vendaluxo.com</div>
      <div class="gap"></div>
      <div>VENDALUXO SRL</div>
      <div>Alameda Business Plaza</div>
      <div>Calle Los Robles 412, Ensanche Norte</div>
      <div>Puerto Claro, Costa Verde</div>
      <div class="gap"></div>
      <div>(555) 310 4720</div>
      <div>info@vendaluxo.com</div>
      <div class="link">www.vendaluxo.com</div>
      <div class="gap"></div>
      <div>VENDALUXO SRL</div>
      <div>Member firm of vendaluxo LLC</div>
    </div>
    <span class="brand-name">vendaluxo<span class="dot"></span></span>
    <svg class="band" width="219" height="8" viewBox="0 0 219 8">
      <path d="M0 2 H124 Q128 2 130 1 L131 3 Q128 4 124 4 H0Z" fill="var(--ink)"/>
      <path d="M124 8 Q134 0 146 0 H219 V8Z" fill="var(--blue)"/>
      <path d="M0 4 H130 L128 6 H0Z" fill="var(--blue)"/>
    </svg>
    <span class="tagline">Consultancy • Audit • Analytics</span>
  </section>

  <!-- envelope front -->
  <section class="piece envelope-front">
    <span class="brand-name">vendaluxo<span class="dot"></span></span>
    <div class="address">
      Alameda Business Plaza<br>
      Calle Los Robles 412, Ensanche Norte<br>
      Puerto Claro, Costa Verde<br>
      (555) 310-4720 | info@vendaluxo.com
    </div>
    <svg class="faint-mark" width="140" height="140" viewBox="0 0 140 140"><circle cx="70" cy="70" r="70" fill="var(--faint)" opacity=".7"/></svg>
    <svg class="band" width="562" height="22" viewBox="0 0 562 22">
      <path d="M0 8 H368 Q374 8 378 5 L380 8 Q375 12 368 12 H0Z" fill="var(--ink)"/>
      <path d="M0 13 H372 L368 16 H0Z" fill="var(--blue)"/>
      <path d="M366 22 Q380 2 404 2 H562 V22Z" fill="var(--blue)"/>
    </svg>
    <span class="band-url">www.vendaluxo.com</span>
  </section>

  <!-- envelope back -->
  <section class="piece envelope-back">
    <div class="texture" role="img" aria-label="Faint repeating ring texture across the envelope back"></div>
    <svg class="flap" width="560" height="100" viewBox="0 0 560 100" role="img" aria-label="Blue envelope flap with a repeating ring pattern">
      <path d="M0 0 H560 L548 64 Q542 93 512 93 H48 Q18 93 12 64Z" fill="var(--blue)"/>
    </svg>
    <div class="badges">
      <span class="partner-badge" style="width:76px;height:20px;border-radius:10px"></span>
      <span class="partner-badge" style="width:100px;height:20px"></span>
      <span class="partner-badge" style="width:64px;height:20px"></span>
    </div>
  </section>

  <!-- letterhead -->
  <section class="piece letterhead">
    <span class="brand-name">vendaluxo<span class="dot"></span></span>
    <svg class="faint-mark" width="190" height="190" viewBox="0 0 190 190"><circle cx="95" cy="95" r="95" fill="var(--faint)" opacity=".55"/></svg>
    <div class="letter">
      <p class="date">Villa Serena, October 12, 2015</p>
      <p class="recipient">Sr.<br>ANDRES LUNA<br>Web Master<br>City</p>
      <p class="body">Contrary to popular belief, Lorem Ipsum is not simply random text. It has roots in a piece of classical Latin literature from 45 BC, making it over 2000 years old. A scholar at a small college in the hills looked up one of the more obscure Latin words, consectetur, from a Lorem Ipsum passage, and going through the cites of the word in classical literature,</p>
      <p class="body">discovered the undoubtable source. Lorem Ipsum comes from sections 1.10.32 and 1.10.33 of "de Finibus Bonorum et Malorum" (The Extremes of Good and Evil) by an ancient author, written in 45 BC. This book is a treatise on the theory of ethics, very popular during the Renaissance. The first line of Lorem Ipsum, "Lorem ipsum dolor sit amet..", comes from a line in section 1.10.32.</p>
      <p class="body">The standard chunk of Lorem Ipsum used since the 1500s is reproduced below for those interested. Sections 1.10.32 and 1.10.33 from "de Finibus Bonorum et Malorum" by the same author are also reproduced in their exact original form, accompanied by English versions from the 1914 translation by a later translator.</p>
      <p class="body">There are many variations of passages of Lorem Ipsum available, but the majority have suffered alteration in some form, by injected humour, or randomised words which don't look even slightly believable. If you are going to use a passage of Lorem Ipsum, you need to be sure there isn't anything embarrassing hidden in the middle of text.</p>
    </div>
    <div class="signature" role="img" aria-label="Handwritten signature of the sender"></div>
    <div class="footer">
      <div class="col" style="left:42px;top:0"><strong>Administration Office</strong><br>Alameda Business Plaza<br>Calle Los Robles 412, Ensanche Norte<br>Puerto Claro, Costa Verde</div>
      <div class="col" style="left:205px;top:3px"><strong>Global Sales</strong><br>780 Harbor Point Drive, Suite C4<br>Eastbay, Oregon 97001<br>United States</div>
      <div class="col" style="left:359px;top:0"><strong>Operations</strong><br>Torre Atlas Work<br>Av. Central 210, Mirador<br>Puerto Claro, Costa Verde</div>
    </div>
    <svg class="band" width="522" height="22" viewBox="0 0 522 22">
      <path d="M0 8 H342 Q348 8 352 5 L354 8 Q349 12 342 12 H0Z" fill="var(--ink)"/>
      <path d="M0 13 H346 L342 16 H0Z" fill="var(--blue)"/>
      <path d="M340 22 Q354 2 378 2 H522 V22Z" fill="var(--blue)"/>
    </svg>
    <span class="band-url">www.vendaluxo.com</span>
  </section>

</div>
</body>
</html>
```